card design for engineering consultancy

engineering drafting and project management company the provides drafting services for.
Electrical, Hydraulic, Mechanical, and Civil services
The company is called Q7R Services and logo is as attached
Information on card should be.
1. Logo
2.website : Q7RServices.example
3. email : info@Q7RServices.example
4. Phone: (+61) 400512836
5. Motto: Design - Document - Develop - Deliver

this card should be basically used for business identification only

Target Market(s)

electricians plumbers air conditioning installers and civil contractors

Industry/Entity Type

engineering, drafting, electrical, plumbing, airconditioning, civil

Contact Information for Business Card

1. Logo 2.website : Q7RServices.example 3. email : info@Q7RServices.example 4. Phone: (+61) 400512836 5. Motto: Design - Document - Develop - Deliver

Font styles to use
Serif

Requirements
Must have
• logo
Nice to have
• something inovative and different that makes it stand out from being just another business card

```html
<!DOCTYPE html>
<html lang="en">
<head>
<meta charset="utf-8">
<title>Q7R Services – Business Card</title>
<link rel="stylesheet" href="https://fonts.googleapis.com/css2?family=Poppins:wght@400;500;600&display=swap">
<style>
  :root {
    --backdrop: #e7e7e7;
    --card: #ffffff;
    --charcoal: #54504f;
    --red: #cf1925;
    --white: #ffffff;
  }
  * { margin: 0; padding: 0; box-sizing: border-box; }
  html, body {
    width: 1200px;
    height: 1200px;
    overflow: hidden;
    background: var(--backdrop);
    font-family: "Poppins", sans-serif;
  }
  .canvas { position: relative; width: 1200px; height: 1200px; }
  .card {
    position: absolute;
    left: 158px;
    width: 884px;
    height: 505px;
    background: var(--card);
    overflow: hidden;
  }
  .card--front { top: 71px; }
  .card--back { top: 624px; }
  .card__shapes { position: absolute; inset: 0; }

  .brand {
    position: absolute;
    left: 0;
    right: 0;
    display: flex;
    align-items: center;
    justify-content: center;
    gap: 18px;
  }
  .brand__mark {
    width: 38px;
    height: 38px;
    background: var(--red);
  }
  .brand__name {
    font-weight: 600;
    color: var(--charcoal);
    letter-spacing: 0.06em;
    text-transform: uppercase;
    white-space: nowrap;
  }
  .card--front .brand { top: 150px; }
  .card--front .brand__name { font-size: 64px; }
  .card--back .brand { top: 128px; }
  .card--back .brand__mark { width: 30px; height: 30px; }
  .card--back .brand__name { font-size: 48px; }

  .front__website {
    position: absolute;
    top: 416px;
    left: 0;
    right: 0;
    text-align: center;
    font-size: 21px;
    font-weight: 600;
    letter-spacing: 0.2em;
    color: var(--charcoal);
  }

  .motto {
    position: absolute;
    left: 40px;
    width: 400px;
    top: 320px;
    text-align: center;
    color: var(--white);
    font-size: 26px;
    line-height: 37px;
    letter-spacing: -0.01em;
    text-transform: uppercase;
  }

  .contacts {
    position: absolute;
    left: 532px;
    top: 325px;
    list-style: none;
    color: var(--white);
    font-size: 19px;
  }
  .contacts__item {
    display: flex;
    align-items: center;
    gap: 9px;
    height: 32px;
  }
  .contacts__icon { width: 19px; height: 19px; flex: none; }
</style>
</head>
<body>
<main class="canvas">

  <section class="card card--front" aria-label="Card front">
    <svg class="card__shapes" width="884" height="505" viewBox="0 0 884 505" aria-hidden="true">
      <polygon points="0,47 208,47 200,62 0,62" fill="var(--red)"/>
      <polygon points="684,443 884,443 884,457 675,457" fill="var(--charcoal)"/>
    </svg>
    <div class="brand">
      <span class="brand__mark"></span>
      <span class="brand__name">Q7R Services</span>
    </div>
    <p class="front__website">Q7RServices.example</p>
  </section>

  <section class="card card--back" aria-label="Card back">
    <svg class="card__shapes" width="884" height="505" viewBox="0 0 884 505" aria-hidden="true">
      <polygon points="0,250 208,250 200,264 0,264" fill="var(--red)"/>
      <polygon points="0,276 495,276 399,452 0,452" fill="var(--charcoal)"/>
      <polygon points="528,276 884,276 884,452 431,452" fill="var(--red)"/>
      <polygon points="684,463 884,463 884,477 675,477" fill="var(--charcoal)"/>
    </svg>
    <div class="brand">
      <span class="brand__mark"></span>
      <span class="brand__name">Q7R Services</span>
    </div>

    <p class="motto">Design – Document –<br>Develop – Deliver</p>

    <ul class="contacts">
      <li class="contacts__item">
        <svg class="contacts__icon" viewBox="0 0 20 20" aria-hidden="true">
          <circle cx="10" cy="10" r="10" fill="var(--white)"/>
          <path d="M6.2 5.2l2 -0.4 1.1 2.6-1.3 1c.7 1.4 1.7 2.4 3 3l1-1.3 2.6 1.1-.4 2c-4.4.2-8.1-3.6-8-8z" fill="var(--red)"/>
        </svg>
        <span>(+61) 400512836</span>
      </li>
      <li class="contacts__item">
        <svg class="contacts__icon" viewBox="0 0 20 20" aria-hidden="true">
          <circle cx="10" cy="10" r="10" fill="var(--white)"/>
          <g fill="none" stroke="var(--red)" stroke-width="1.1">
            <circle cx="10" cy="10" r="5.5"/>
            <ellipse cx="10" cy="10" rx="2.4" ry="5.5"/>
            <line x1="4.5" y1="10" x2="15.5" y2="10"/>
          </g>
        </svg>
        <span>Q7RServices.example</span>
      </li>
      <li class="contacts__item">
        <svg class="contacts__icon" viewBox="0 0 20 20" aria-hidden="true">
          <circle cx="10" cy="10" r="10" fill="var(--white)"/>
          <rect x="5" y="6.5" width="10" height="7" fill="var(--red)"/>
          <polyline points="5.3,7 10,10.6 14.7,7" fill="none" stroke="var(--white)" stroke-width="1"/>
        </svg>
        <span>info@Q7RServices.example</span>
      </li>
    </ul>
  </section>

</main>
</body>
</html>
```